Designs for a fundrasining event a Brown Tie Beer and Wine event

We need a flyer, brochure, and tickets for entry for a brown tie event that will be a beer and wine pairing fundraising event to be held on May 9th from 6pm to 10pm at the Maplecrest Restaurant in Cedar Lake, Indiana, USA. There will be approximately 10 silent auction items and 5 or so sponsors that we will want to have the logos of the sponsors on what we can as well, attached are the logo for Open Hearth Foundation, IV NFP, which is the nonprofit hosting the event, there is also a logo for Dunmore Law, LLC which is one of the sponsors (this is so you have an idea of the other 4 or so that we would also want incorporated somehow). Please ask as many questions as you may have to clarify.

Industry/Entity Type

Event

Contact Information for Business Card

Open Hearth
Wendy P. Halvorsen
President/CEO
(555)384-9062
www.openhearthfdn.example.org

New Card:
Marcus J. Halvorsen
Director
(555)627-3148
www.openhearthfdn.example.org

New Card:
Norma T. Halvorsen
Director
www.openhearthfdn.example.org

New Card:
Gerald K. Halvorsen
Director
www.openhearthfdn.example.org

Font styles to use
Script

Requirements
Must have
• I want a clean card for all 4 individuals with the logo that was attached.

```html
<!DOCTYPE html>
<html lang="en">
<head>
<meta charset="utf-8">
<title>Beer Wine Fundraising Event</title>
<link rel="stylesheet" href="https://fonts.googleapis.com/css2?family=Cinzel:wght@400;700&family=Exo+2:wght@400;500&family=Cormorant+Garamond:wght@500&display=swap">
<style>
  :root {
    --gold: #f2c81a;
    --red: #d0121b;
    --panel: rgba(12, 6, 4, 0.78);
    --white: #ffffff;
    --black: #050505;
    --ink: #1e1e1e;
    --coin: #c9c9c9;
  }
  html, body { margin: 0; padding: 0; overflow: hidden; }
  body { width: 848px; height: 1200px; position: relative; background: #2a1208; }
  .backdrop {
    position: absolute; inset: 0;
    background:
      radial-gradient(ellipse 260px 120px at 290px 40px, #efe6d6 0%, rgba(239,230,214,0) 100%),
      radial-gradient(ellipse 220px 420px at 60px 700px, #e39a1c 0%, rgba(227,154,28,0) 100%),
      linear-gradient(180deg, #e8b23a 0%, #b86d12 25%, #5a1a0c 55%, #3a140a 80%, #6b3a1c 100%);
  }
  .panel {
    position: absolute; left: 52px; top: 70px; width: 743px; height: 975px;
    background: var(--panel);
  }
  .title {
    position: absolute; left: 60px; top: 76px; margin: 0;
    font-family: "Cinzel", serif; font-weight: 400; font-size: 132px;
    line-height: 1; letter-spacing: -2px; white-space: nowrap;
  }
  .title .beer { color: var(--gold); }
  .title .wine { color: var(--red); }
  .subtitle {
    position: absolute; left: 64px; top: 219px; width: 715px;
    display: flex; align-items: center; gap: 14px;
    font-family: "Cinzel", serif; font-weight: 700; font-size: 17px;
    color: var(--white); letter-spacing: 0.5px;
  }
  .subtitle::before, .subtitle::after {
    content: ""; flex: 1; height: 1px; background: rgba(255,255,255,0.55);
  }
  .subtitle::before { flex: 0 0 230px; }
  .details {
    position: absolute; left: 0; width: 848px; top: 248px; text-align: center;
    font-family: "Exo 2", sans-serif; font-size: 17px; color: var(--white);
  }
  .headline {
    position: absolute; left: 0; width: 848px; text-align: center;
    font-family: "Cinzel", serif; font-weight: 400; margin: 0; line-height: 1;
  }
  .headline.tasting { top: 340px; font-size: 66px; color: var(--gold); }
  .headline.with { top: 425px; font-size: 58px; color: var(--gold); }
  .headline.appetizers { top: 525px; font-size: 86px; color: var(--red); }
  .badge {
    position: absolute; border-radius: 50%; overflow: hidden;
    font-family: "Exo 2", sans-serif; text-align: center;
  }
  .badge.tickets { left: 85px; top: 690px; width: 302px; height: 302px; background: var(--white); color: var(--black); }
  .badge.contact { left: 430px; top: 683px; width: 327px; height: 327px; background: var(--black); color: var(--white); border: 1px solid rgba(255,255,255,0.25); }
  .coins { position: absolute; left: 25px; top: 110px; width: 250px; height: 140px; }
  .tickets .label { position: absolute; top: 58px; width: 100%; font-size: 34px; }
  .tickets .price { position: absolute; top: 92px; width: 100%; font-size: 102px; letter-spacing: -2px; }
  .contact .phone-icon { position: absolute; left: 40px; top: 40px; width: 230px; height: 230px; }
  .contact .text { position: absolute; top: 92px; width: 100%; font-size: 36px; line-height: 1.33; }
  .sponsors-note {
    position: absolute; left: 0; width: 848px; top: 1018px; text-align: center;
    font-family: "Exo 2", sans-serif; font-size: 15px; color: var(--white);
  }
  .sponsor-band {
    position: absolute; left: 52px; top: 1045px; width: 743px; height: 98px; background: var(--white);
    display: flex; align-items: center; justify-content: center; gap: 14px;
  }
  .sponsor-mark { width: 36px; height: 36px; border: 1.5px solid var(--ink); border-radius: 50%; }
  .sponsor-name {
    font-family: "Cormorant Garamond", serif; font-weight: 500; font-size: 25px;
    color: var(--ink); letter-spacing: 1px; text-transform: uppercase;
  }
</style>
</head>
<body>
  <div class="backdrop" role="img" aria-label="Photograph of frothy mugs of amber and dark beer on a wooden table"></div>
  <div class="panel"></div>

  <h1 class="title"><span class="beer">BEER</span><span class="wine">WINE</span></h1>
  <div class="subtitle">FUNDRAISING EVENT</div>
  <p class="details" style="margin:0">May 9th from 6pm to 10pm, Maplecrest Restaurant, Cedar Lake, Indiana, USA</p>

  <h2 class="headline tasting">TASTING</h2>
  <h2 class="headline with">WITH</h2>
  <h2 class="headline appetizers">APPETIZERS</h2>

  <div class="badge tickets">
    <div class="coins" role="img" aria-label="Illustration of stacked silver dollar coins" style="background: radial-gradient(ellipse at center, #cfcfcf 0%, rgba(207,207,207,0.6) 60%, rgba(255,255,255,0) 100%);"></div>
    <div class="label">Tickets</div>
    <div class="price">$100</div>
  </div>

  <div class="badge contact">
    <svg class="phone-icon" viewBox="0 0 24 24" aria-hidden="true">
      <path fill="#2a2a2a" d="M6.6 10.8c1.4 2.8 3.8 5.1 6.6 6.6l2.2-2.2c.3-.3.7-.4 1-.2 1.1.4 2.3.6 3.6.6.6 0 1 .4 1 1V20c0 .6-.4 1-1 1C10.6 21 3 13.4 3 4c0-.6.4-1 1-1h3.5c.6 0 1 .4 1 1 0 1.2.2 2.4.6 3.6.1.3 0 .7-.2 1z"/>
    </svg>
    <div class="text">Contact us<br>at<br>555-384-9062</div>
  </div>

  <p class="sponsors-note" style="margin:0">Sponsors include</p>
  <div class="sponsor-band">
    <span class="sponsor-mark"></span>
    <span class="sponsor-name">Dunmore Law, LLC</span>
  </div>
</body>
</html>
```